A website for a green bio-plastics manufacturing company

We need a home page designed and two complimentary template pages that can be used for the rest of the website. The template page should vary in design from the home page, but should flow uniformly with it.

This is a very innovative company with a proprietary manufacturing method of using bird feathers to make plastic.

The site should be functional, informative, user-friendly and informative to both our business partners and the consumers.
Updates

I've added a more concise overview of the company.  If any of the designers have any questions for me, please ask.  Thanks

Felix

Target Market(s)

Business partners interested in using bio-plastics for their products and general customers.

Industry/Entity Type

Manufacturing

Number of Pages Required

3 pages

Requirements
Must have
• I attached some information about the company, so the site should be designed to incorporate that content.

Will need to be edited by Adobe Contribute.

Easy to navigate

One of the template pages should have one column for content. The other should have two columns. I''m open to different ideas though.

Should be very pleasing to the eye and uncluttered.

Want to be informative to both our business partners as well as consumers who may be researching our product(s)

Easy to Maintain

Anticipated Tabs/Pages
· Home Page
o General “welcome” page

· About Us
o Company overview and information

· Products
o Horticulture Containers
o Agriculture Films
o Where to Buy
o Upcoming Products

· Business Partners

· Press Releases

· Contact Us

Nice to have
• Would like to have earth tones and or nice greens in the color scheme. They make use of bird feathers for their manufacturing process, so perhaps a real sharp image of a feather can be incorporated into the design. Be creative though.

Perhaps a jQuery nav bar, but that may be out of scope.

Should not have
• No flash at all.

```html
<!DOCTYPE html>
<html lang="en">
<head>
<meta charset="utf-8">
<title>Northfield Bioplastics – Business Partners</title>
<link rel="stylesheet" href="https://fonts.googleapis.com/css2?family=Arimo:wght@400;700&family=PT+Sans:wght@400;700&family=Roboto:wght@300;400&family=Open+Sans:ital,wght@0,400;1,700&display=swap">
<style>
  :root {
    --ink: #1a1a1a;
    --body-ink: #2b2b2b;
    --leaf: #8aa51a;
    --leaf-dark: #6e9200;
    --leaf-light: #b3cf2a;
    --hero-rule: #c5d09a;
    --accent: #ee5b0c;
    --button-top: #ffb12a;
    --button-bottom: #ffd21a;
    --button-text: #b5260a;
    --footer-bg: #eff0ea;
    --footer-rule: #c2c9ad;
    --divider: #dcdcdc;
    --feather: #dde4cf;
    --logo-green: #1e7a3a;
  }
  * { box-sizing: border-box; margin: 0; padding: 0; }
  html, body { width: 1023px; height: 1200px; overflow: hidden; background: #fff; }
  body { position: relative; font-family: "Open Sans", Verdana, sans-serif; color: var(--body-ink); }

  .site-header { position: absolute; left: 0; top: 0; width: 1023px; height: 121px; }
  .brand { position: absolute; left: 36px; top: 14px; display: flex; align-items: center; gap: 14px; }
  .brand-mark { width: 70px; height: 70px; border-radius: 50%; background: var(--logo-green); }
  .brand-name { font-family: "Arimo", Arial, sans-serif; font-weight: 400; font-size: 33px; line-height: 34px; color: var(--ink); letter-spacing: 0.5px; }

  .main-nav { position: absolute; top: 70px; left: 0; width: 1023px; font-family: "Arimo", Arial, sans-serif; font-size: 14px; }
  .main-nav a { position: absolute; color: var(--ink); text-decoration: none; white-space: nowrap; }
  .main-nav a::after { content: ""; display: inline-block; margin-left: 4px; width: 0; height: 0; border-left: 5px solid var(--accent); border-top: 3px solid transparent; border-bottom: 3px solid transparent; vertical-align: 2px; }
  .main-nav a.is-current { color: var(--leaf); }

  .hero { position: absolute; left: 33px; top: 121px; width: 973px; height: 316px; background: linear-gradient(90deg, #a5c224 0%, #93b414 55%, #7ea208 100%); border-bottom: 3px solid var(--hero-rule); overflow: hidden; }
  .hero-art { position: absolute; left: 0; top: 0; width: 580px; height: 313px; background: radial-gradient(circle at 260px 140px, #c9dd1e 0, #7fa815 90px, #4f8a14 145px, rgba(165,194,36,0) 190px), linear-gradient(90deg, rgba(200,215,120,0.5), rgba(165,194,36,0)); }
  .hero-title { position: absolute; left: 492px; top: 44px; font-family: "Roboto", Arial, sans-serif; font-weight: 300; font-size: 45px; color: #fff; letter-spacing: -1.5px; text-shadow: 0 1px 2px rgba(0,0,0,0.25); }
  .hero-lead { position: absolute; left: 496px; top: 126px; width: 440px; font-family: "Roboto", Arial, sans-serif; font-weight: 300; font-size: 23px; line-height: 25px; color: #fff; text-shadow: 0 1px 2px rgba(0,0,0,0.25); }
  .hero-button { position: absolute; left: 585px; top: 223px; width: 335px; height: 43px; border-radius: 3px; background: linear-gradient(180deg, var(--button-top), var(--button-bottom)); border: 1px solid #f08a10; color: var(--button-text); font-family: "Arimo", Arial, sans-serif; font-size: 16px; line-height: 41px; text-align: center; text-decoration: none; }

  .content { position: absolute; left: 62px; top: 494px; width: 915px; }
  .page-title { font-family: "PT Sans", Arial, sans-serif; font-weight: 400; font-size: 25px; letter-spacing: -0.5px; color: var(--ink); display: flex; align-items: center; gap: 8px; height: 30px; margin-bottom: 12px; }
  .entry { font-size: 11px; line-height: 15px; margin-bottom: 15px; }
  .entry h2 { font-size: 11px; font-style: italic; font-weight: 700; color: var(--ink); }
  .contact-line { font-size: 11px; line-height: 15px; }
  .contact-line b { font-style: italic; }
  .contact-line a { color: var(--accent); }
  .section-divider { position: absolute; left: 333px; top: 666px; width: 387px; height: 1px; background: var(--divider); }

  .feather-band { position: absolute; left: 33px; top: 1025px; width: 973px; height: 72px; background: linear-gradient(180deg, rgba(221,228,207,0) 0%, var(--feather) 60%, #e6eadc 100%); }

  .site-footer { position: absolute; left: 33px; top: 1097px; width: 973px; height: 103px; background: var(--footer-bg); border-top: 3px solid var(--footer-rule); font-size: 12px; color: var(--ink); }
  .footer-nav { position: absolute; left: 30px; top: 25px; }
  .footer-nav a { color: var(--ink); text-decoration: none; }
  .footer-nav span { margin: 0 7px; }
  .footer-legal { position: absolute; right: 14px; top: 27px; font-size: 11px; letter-spacing: 0.3px; }
  .footer-legal a { color: var(--ink); }
</style>
</head>
<body>
  <header class="site-header">
    <div class="brand">
      <span class="brand-mark"></span>
      <span class="brand-name">NORTHFIELD<br>BIOPLASTICS</span>
    </div>
    <nav class="main-nav">
      <a class="is-current" href="#" style="left:407px">About Us</a>
      <a href="#" style="left:516px">Products</a>
      <a href="#" style="left:627px">Business Partners</a>
      <a href="#" style="left:784px">Press Releases</a>
      <a href="#" style="left:937px">Contacts</a>
    </nav>
  </header>

  <section class="hero">
    <div class="hero-art" role="img" aria-label="Green globe resting on grass with a feather and falling petals"></div>
    <h1 class="hero-title">Welcome to Our Site!</h1>
    <p class="hero-lead">Sed ut perspiciatis unde omnis iste natus error sit voluptatem accustium doremque launtium.</p>
    <a class="hero-button" href="#">CLICK HERE TO LEARN MORE</a>
  </section>

  <main class="content">
    <h1 class="page-title">Business Partners
      <svg width="19" height="19" viewBox="0 0 19 19" aria-hidden="true"><circle cx="9.5" cy="9.5" r="9.5" fill="#ee5b0c"/><path d="M5 9.5h8M9.5 5.5l4 4-4 4" stroke="#fff" stroke-width="2" fill="none"/></svg>
    </h1>
    <article class="entry">
      <h2>Lorem ipsum dolor sit amet, consectetuer adipiscing elit.</h2>
      <p>Praesent vestibulum molestie lacus. Aenean nonummy hendrerit mauris. Phasellus porta. Fusce suscipit varius mi. Cum sociis natoque penatibus et magnis dis parturient montes, nascetur ridiculus mus. Nulla dui. Fusce feugiat malesuada odio. Morbi nunc odio, gravida at, cursus nec, luctus a, lorem. Maecenas tristique orci ac sem. Duis ultricies pharetra magna. Donec accumsan malesuada orci.</p>
    </article>
    <article class="entry">
      <h2>Donec sit amet eros. Lorem ipsum dolor sit amet, consectetuer adipiscing elit.</h2>
      <p>Mauris fermentum dictum magna. Sed laoreet aliquam leo. Ut tellus dolor, dapibus eget, elementum vel, cursus eleifend, elit. Aenean auctor wisi et urna. Aliquam erat volutpat. Duis ac turpis. Integer rutrum ante eu lacus.</p>
    </article>
    <article class="entry">
      <h2>Lesuada at, neque. Vivamus eget nibh. Etiam cursus leo vel metus.</h2>
      <p>Nulla facilisi. Aenean nec eros. Vestibulum ante ipsum primis in faucibus orci luctus et ultrices posuere cubilia Curae; Suspendisse sollicitudin velit sed leo. Ut pharetra augue nec augue. Nam elit magna, hendrerit sit amet, tincidunt ac, viverra sed, nulla. Donec porta diam eu massa. Quisque diam lorem, interdum vitae, dapibus ac, scelerisque vitae, pede. Donec eget tellus non erat lacinia fermentum. Donec in velit vel ipsum auctor pulvinar. Proin ullamcorper urna et felis.</p>
    </article>
    <article class="entry">
      <h2>Vestibulum iaculis lacinia est. Proin dictum elementum velit. Fusce euismod consequat ante.</h2>
      <p>Lorem ipsum dolor sit amet, consectetuer adipiscing elit. Pellentesque sed dolor. Aliquam congue fermentum nisl. Mauris accumsan nulla vel diam. Sed in lacus ut enim adipiscing aliquet. Nulla venenatis. In pede mi, aliquet sit amet, euismod in, auctor ut, ligula. Aliquam dapibus tincidunt metus. Praesent justo dolor, lobortis quis, lobortis dignissim, pulvinar ac, lorem. Vestibulum sed ante. Donec sagittis euismod purus.</p>
    </article>
    <article class="entry">
      <h2>Sed ut perspiciatis unde omnis iste natus error sit voluptatem.</h2>
      <p>Accusantium doloremque laudantium, totam rem aperiam, eaque ipsa quae ab illo inventore veritatis et quasi architecto beatae vitae dicta sunt explicabo. Nemo enim ipsam voluptatem quia voluptas sit aspernatur aut odit aut fugit, sed quia consequuntur magni dolores eos qui ratione voluptatem sequi nesciunt. Neque porro quisquam est, qui dolorem ipsum quia dolor sit amet, consectetur, adipisci velit, sed quia non numquam eius modi tempora incidunt ut labore et dolore magnam aliquam quaerat voluptatem.</p>
    </article>
    <article class="entry">
      <h2>Lorem ipsum dolor sit amet, consectetuer adipiscing elit.</h2>
      <p>Praesent vestibulum molestie lacus. Aenean nonummy hendrerit mauris. Phasellus porta. Fusce suscipit varius mi. Cum sociis natoque penatibus et magnis dis parturient montes, nascetur ridiculus mus. Nulla dui. Fusce feugiat malesuada odio. Morbi nunc odio, gravida at, cursus nec, luctus a, lorem. Maecenas tristique orci ac sem. Duis ultricies pharetra magna. Donec accumsan malesuada orci.</p>
    </article>
    <p class="contact-line"><b>E-mail:</b> <a href="#">info@northfieldbio.com</a></p>
  </main>
  <div class="section-divider"></div>

  <div class="feather-band" role="img" aria-label="Row of soft pale feathers"></div>

  <footer class="site-footer">
    <nav class="footer-nav">
      <a href="#">Company</a><span>|</span><a href="#">Products</a><span>|</span><a href="#">Business Partners</a><span>&nbsp;|</span><a href="#">Support</a><span>|</span><a href="#">Contacts</a>
    </nav>
    <p class="footer-legal">NORTHFIELD BIOPLASTICS &nbsp; 2010 | <a href="#">Privacy Policy</a></p>
  </footer>
</body>
</html>
```